Professional Services Business Card Design

We need a business card design for a relatively new (less than one year old) company. Harrowmere Advisory Partners, LLC provides professional support services and expert assistance in acquisition management to federal agencies, and also provides acquisition workforce personnel training and development for defense and civilian agencies. The colors used should incorporate the colors found within the company's logo, which is attached.

Font styles to use
Serif
Sans Serif

```html
<!DOCTYPE html>
<html lang="en">
<head>
<meta charset="utf-8">
<title>Harrowmere Advisory Partners — Business Card</title>
<link rel="stylesheet" href="https://fonts.googleapis.com/css2?family=Cinzel:wght@400;500&family=Roboto+Condensed:wght@400;700&display=swap">
<style>
  :root {
    --navy: #363b59;
    --navy-deep: #2c3049;
    --paper: #f6f6f4;
    --ink: #2f3350;
    --backdrop: #4a4a4c;
    --white: #ffffff;
  }
  * { box-sizing: border-box; margin: 0; padding: 0; }
  html, body { width: 1200px; height: 927px; overflow: hidden; }
  body {
    background: var(--backdrop);
    display: flex;
    align-items: center;
    justify-content: center;
    gap: 60px;
    font-family: "Roboto Condensed", Arial, sans-serif;
  }
  .card {
    width: 520px;
    height: 297px;
    position: relative;
    overflow: hidden;
    box-shadow: 0 10px 28px rgba(0,0,0,.35);
  }

  /* Front */
  .card--front {
    background: linear-gradient(160deg, var(--navy) 0%, var(--navy-deep) 100%);
    display: flex;
    align-items: center;
    justify-content: center;
  }
  .front-name {
    font-family: "Cinzel", Georgia, serif;
    font-weight: 500;
    color: var(--white);
    text-align: center;
    font-size: 26px;
    line-height: 1.3;
    letter-spacing: 2px;
  }

  /* Back */
  .card--back { background: var(--paper); }
  .band {
    position: absolute;
    left: 0; right: 0;
    top: 30px;
    height: 70px;
    background: var(--navy);
  }
  .band__name {
    position: absolute;
    right: 26px;
    top: 14px;
    font-family: "Cinzel", Georgia, serif;
    color: var(--white);
    text-align: left;
    font-size: 19px;
    line-height: 1.05;
    letter-spacing: 1.5px;
  }
  .band__name small {
    display: block;
    font-size: 11.5px;
    letter-spacing: 1.2px;
  }
  .contacts {
    position: absolute;
    left: 244px;
    top: 112px;
    list-style: none;
    color: var(--ink);
    font-size: 12.5px;
  }
  .contacts li {
    display: flex;
    align-items: flex-start;
    gap: 7px;
    margin-bottom: 5px;
    line-height: 1.2;
  }
  .contacts .icon {
    flex: none;
    width: 14px; height: 14px;
    border-radius: 50%;
    background: var(--ink);
    display: flex; align-items: center; justify-content: center;
    margin-top: 1px;
  }
  .contacts svg { width: 9px; height: 9px; }
  .holder {
    position: absolute;
    left: 34px;
    bottom: 40px;
    color: var(--ink);
  }
  .holder__name {
    font-weight: 700;
    font-size: 17px;
    letter-spacing: .3px;
    text-transform: uppercase;
  }
  .holder__role { font-size: 12.5px; }
</style>
</head>
<body>

  <section class="card card--front" aria-label="Card front">
    <p class="front-name">Harrowmere<br>Advisory Partners</p>
  </section>

  <section class="card card--back" aria-label="Card back">
    <div class="band">
      <p class="band__name">Harrowmere<small>Advisory Partners, LLC</small></p>
    </div>

    <ul class="contacts">
      <li>
        <span class="icon"><svg viewBox="0 0 10 10"><path d="M5 1a3 3 0 0 1 3 3c0 2-3 5-3 5S2 6 2 4a3 3 0 0 1 3-3z" fill="#fff"/><circle cx="5" cy="4" r="1" fill="#2f3350"/></svg></span>
        <span>48 Larkspur Row, Unit 7,<br>Fenwick Hollow, ZZ 00000</span>
      </li>
      <li>
        <span class="icon"><svg viewBox="0 0 10 10"><rect x="2" y="2.5" width="6" height="5" rx="1" fill="#fff"/></svg></span>
        <span>011 - 48 27 60 13</span>
      </li>
      <li>
        <span class="icon"><svg viewBox="0 0 10 10"><path d="M2.5 1.5l1.8 0 .6 2-1 .8a5 5 0 0 0 1.8 1.8l.8-1 2 .6v1.8A1 1 0 0 1 7.5 8.5 6 6 0 0 1 1.5 2.5a1 1 0 0 1 1-1z" fill="#fff"/></svg></span>
        <span>011 - 48 27 60 13</span>
      </li>
      <li>
        <span class="icon"><svg viewBox="0 0 10 10"><rect x="1.5" y="2.5" width="7" height="5" fill="none" stroke="#fff" stroke-width="1"/><path d="M1.5 2.5L5 5.5l3.5-3" fill="none" stroke="#fff" stroke-width="1"/></svg></span>
        <span>devon@harrowmereadvisory.com</span>
      </li>
      <li>
        <span class="icon"><svg viewBox="0 0 10 10"><circle cx="5" cy="5" r="3.5" fill="none" stroke="#fff" stroke-width="1"/><path d="M1.5 5h7M5 1.5c-1.5 2-1.5 5 0 7M5 1.5c1.5 2 1.5 5 0 7" fill="none" stroke="#fff" stroke-width=".8"/></svg></span>
        <span>www.harrowmereadvisory.com</span>
      </li>
    </ul>

    <div class="holder">
      <p class="holder__name">Devon Ashcroft</p>
      <p class="holder__role">Business Development</p>
    </div>
  </section>

</body>
</html>
```